Health & Wellness Website

Corvantel focuses on helping people with chronic health conditions through communication, education and behavior management. See the attached summary for more info on the company.

The attached wire frames should be turned into a very intuitive and simple website design. The design should have a minimal, modern, and yet still personal feel since the main point of the site is for people with chronic health conditions to be able to express themselves and find others that are like them.

There are 18 pages in the wire frames, but most of them have very similar content and page layouts. The design of the pages should to be as similar to each other as possible with most of the features and formats being repeated. The layout is not set in stone and the primary focus should be on intuitive use.

There should be two versions of the designs: one for tablets in the portrait mode (768 px) and one in the landscape mode (1024 px). These layouts should be included in the winning design.

If you would like to submit one page, I will check the posting and give feedback frequently so you don't waste your time and have to change everything.

Target Market(s)

The target market for this website has two different groups within the overall chronic health patient umbrella. The primary group are people who are under 55 yrs old and already use one or more social media sites. The other group consists of people that are older and less familiar with modern websites. The site needs to be catered to the latter and be incredibly intuitive.

Industry/Entity Type

Education

Requirements
Must have
• INTUITIVE DESIGN that is simple, minimal, and modern with a limited color palette. Tablet landscape and portrait versions are needed. Adobe Fireworks is the preferred program and will give submitted designs a huge leg up in the decision. Adobe Photoshop is the only other acceptable program to use. The designer will also need to make the social media icons, buttons, and other graphic design items that are needed for to go along with the theme. These should be vector graphics and be created either in Adobe Fireworks or Illustrator. All working files for the pages, icons, and graphics will be required once the winner is chosen.
• The necessary pages include: the landing page (long scrolling page with about and community sections); a general modal pop-up layout that includes forms and text; the template for inside of the members area (Home Page in wire frames); the community page; and the profile page (with tabs). Please include all the pages you feel it takes to communicate your design.
Nice to have
• Descriptions of transition effects and notes for the programmers are a good thing. The designer might consider adding navigation on the public landing page that scrolls with the header (This is not in the wire frames).
Should not have
• Flashy or complex features that require a lot of code to accomplish. Should not look like Plaztera.

```html
<!DOCTYPE html>
<html lang="en">
<head>
<meta charset="utf-8">
<title>Corvantel — Health &amp; Wellness</title>
<link rel="stylesheet" href="https://fonts.googleapis.com/css2?family=Arvo:wght@400;700&family=Open+Sans:wght@400;600&family=Josefin+Sans:wght@400;600&display=swap">
<style>
:root{
  --blue:#0a96dc;
  --blue-dark:#0a73b0;
  --header-line:#1a6fa0;
  --ink:#222;
  --text:#555;
  --muted:#8a8a8a;
  --logo:#7a7b8a;
  --field-border:#d4d4d4;
  --sky-top:#cfd9e1;
  --sky-bottom:#eef1f3;
  --page:#eceeef;
  --white:#fff;
}
*{box-sizing:border-box;margin:0;padding:0}
html,body{width:1115px;height:1200px;overflow:hidden}
body{background:var(--page);font-family:"Open Sans",Arial,sans-serif;color:var(--text);position:relative}

/* header */
.site-header{position:absolute;left:0;top:0;width:1115px;height:143px;background:var(--white);border-bottom:2px solid var(--header-line)}
.brand{position:absolute;left:70px;top:30px;display:flex;flex-direction:column;align-items:center;width:206px}
.brand-mark{width:54px;height:54px;background:var(--logo);border-radius:4px}
.brand-name{margin-top:14px;font-family:"Josefin Sans",sans-serif;font-weight:400;font-size:25px;letter-spacing:11px;color:var(--logo)}
.field{position:absolute;top:54px;height:33px;width:286px;display:flex;border:1px solid var(--field-border);background:var(--white)}
.field-icon{width:32px;height:100%;background:var(--blue);display:flex;align-items:center;justify-content:center}
.field-label{padding-left:9px;font-size:11px;color:var(--muted);line-height:31px}
.field-email{left:487px}
.field-password{left:783px}
.btn{display:inline-block;background:var(--blue);color:var(--white);border:1px solid var(--blue-dark);border-radius:2px;text-align:center;font-family:"Open Sans",Arial,sans-serif}
.header-btn{position:absolute;top:96px;height:34px;width:80px;font-size:16px;line-height:32px}
.btn-signup{left:694px}
.btn-login{left:783px}
.remember{position:absolute;left:948px;top:108px;display:flex;align-items:center;font-size:11px;color:var(--muted)}
.remember-box{width:17px;height:17px;background:#4cb3e6;margin-right:6px}

/* hero */
.hero{position:absolute;left:0;top:145px;width:1115px;height:452px;background:radial-gradient(ellipse at 45% 20%,#f7f8f9 0%,var(--sky-bottom) 45%,var(--sky-top) 100%)}
.hero-title{position:absolute;left:51px;top:90px;width:368px;height:60px;background:var(--blue);border-radius:2px;color:var(--white);font-family:"Arvo",serif;font-size:43px;line-height:60px;padding-left:25px}
.hero-subtitle{position:absolute;left:54px;top:165px;font-family:"Arvo",serif;font-size:27px;color:var(--ink);letter-spacing:.5px}
.hero-copy{position:absolute;left:51px;top:217px;width:440px;font-size:13.5px;line-height:20px;letter-spacing:-.6px;color:#555}
.hero-copy p+p{margin-top:20px}
.btn-read{position:absolute;left:50px;top:352px;width:93px;height:34px;line-height:32px;font-size:13px;letter-spacing:-.5px}
.hero-photo{position:absolute;left:572px;top:25px;width:455px;height:427px;background:radial-gradient(ellipse at 50% 55%,#cfe0c4 0%,#b7c7ad 45%,rgba(200,210,215,0) 75%)}

/* newsletter panel */
.panel{position:absolute;left:69px;top:597px;width:990px;height:603px;background:var(--white);box-shadow:0 0 30px rgba(0,0,0,.18)}
.panel-bar{height:12px;background:var(--blue)}
.panel-notch{position:absolute;left:72px;top:12px}
.panel-heading{margin-top:48px;text-align:center;font-family:"Arvo",serif;font-size:36px;color:var(--ink)}
.panel-heading .accent{color:var(--blue)}
.panel-lead{margin-top:8px;text-align:center;font-family:Arial,Helvetica,sans-serif;font-size:20px;color:var(--ink)}
.btn-subscribe{display:block;margin:29px auto 0;width:80px;height:35px;line-height:33px;font-size:14px}
.divider{margin:42px 33px 0;border-top:3px dotted #dcdcdc}
.features{display:grid;grid-template-columns:repeat(3,315px);row-gap:40px;margin:42px 0 0 49px}
.feature-head{display:flex;align-items:center}
.feature-icon{width:40px;height:40px;border-radius:50%;background:#000;display:flex;align-items:center;justify-content:center}
.feature-title{margin-left:20px;font-family:"Arvo",serif;font-weight:700;font-size:14px;color:#333}
.feature-text{margin-top:16px;font-size:11px;line-height:20px;color:#666;width:290px}
</style>
</head>
<body>
<header class="site-header">
  <div class="brand">
    <span class="brand-mark"></span>
    <span class="brand-name">CORVANTEL</span>
  </div>
  <div class="field field-email">
    <span class="field-icon"><svg width="16" height="16" viewBox="0 0 16 16"><circle cx="8" cy="5" r="3.5" fill="#fff"/><path d="M1 16c0-4 3-6.5 7-6.5s7 2.5 7 6.5z" fill="#fff"/></svg></span>
    <span class="field-label">Email</span>
  </div>
  <div class="field field-password">
    <span class="field-icon"><svg width="14" height="16" viewBox="0 0 14 16"><path d="M3.5 7V5a3.5 3.5 0 0 1 7 0v2" stroke="#fff" stroke-width="2" fill="none"/><rect x="1" y="7" width="12" height="9" fill="#fff"/></svg></span>
    <span class="field-label">Password</span>
  </div>
  <span class="btn header-btn btn-signup">Sign Up</span>
  <span class="btn header-btn btn-login">Login</span>
  <label class="remember"><span class="remember-box"></span>Keep me Logged in</label>
</header>

<section class="hero">
  <h1 class="hero-title">Health is imp !</h1>
  <h2 class="hero-subtitle">Chronic health disease</h2>
  <div class="hero-copy">
    <p>Corvantel focuses on helping people with chronic health conditions through communication, education and behavior management. See the attached summary for more info on the company.</p>
    <p>Corvantel focuses on helping people with chronic health conditions through communication, education and behavior management</p>
  </div>
  <span class="btn btn-read">Read more</span>
  <div class="hero-photo" role="img" aria-label="Photo of an older woman holding a coat and handbag"></div>
</section>

<section class="panel">
  <div class="panel-bar"></div>
  <svg class="panel-notch" width="34" height="34" viewBox="0 0 34 34"><path d="M0 0H34L0 34Z" fill="var(--blue)"/></svg>
  <h2 class="panel-heading">Subscribe to <span class="accent">Newsletter</span> for Free</h2>
  <p class="panel-lead">Lorem ipsum dolor slo Vivamus, please contact us for everything you need.</p>
  <span class="btn btn-subscribe">Sign Up</span>
  <div class="divider"></div>
  <div class="features">
    <article class="feature"><div class="feature-head"><span class="feature-icon"><svg width="12" height="14"><rect x="1" y="1" width="10" height="12" fill="none" stroke="#fff"/></svg></span><h3 class="feature-title">About Corvantel</h3></div><p class="feature-text">Lorem ipsum dolor slo onsec tueraliquet Morbi nec In Curabitur lreaoreet nisl lorem in pellente pellente eget. Lorem ipsum dolor slo onsec Vivamus....</p></article>
    <article class="feature"><div class="feature-head"><span class="feature-icon"><svg width="12" height="14"><rect x="1" y="1" width="10" height="12" fill="none" stroke="#fff"/></svg></span><h3 class="feature-title">About Corvantel</h3></div><p class="feature-text">orem ipsum dolor slo onsec tueraliquet Morbi nec In Curabitur lreaoreet nisl lorem in pellente pellente eget. Lorem ipsum dolor slo onsec Vivamus....</p></article>
    <article class="feature"><div class="feature-head"><span class="feature-icon"><svg width="12" height="14"><rect x="1" y="1" width="10" height="12" fill="none" stroke="#fff"/></svg></span><h3 class="feature-title">About Corvantel</h3></div><p class="feature-text">Lorem ipsum dolor slo onsec tueraliquet Morbi nec In Curabitur lreaoreet nisl lorem in pellente pellente eget. Lorem ipsum dolor slo onsec Vivamus....</p></article>
    <article class="feature"><div class="feature-head"><span class="feature-icon"><svg width="12" height="14"><rect x="1" y="1" width="10" height="12" fill="none" stroke="#fff"/></svg></span><h3 class="feature-title">Community Highlights</h3></div><p class="feature-text">Lorem ipsum dolor slo onsec tueraliquet Morbi nec In Curabitur lreaoreet nisl lorem in pellente pellente eget. Lorem ipsum dolor slo onsec Vivamus....</p></article>
    <article class="feature"><div class="feature-head"><span class="feature-icon"><svg width="12" height="14"><rect x="1" y="1" width="10" height="12" fill="none" stroke="#fff"/></svg></span><h3 class="feature-title">Community Highlights</h3></div><p class="feature-text">Lorem ipsum dolor slo onsec tueraliquet Morbi nec In Curabitur lreaoreet nisl lorem in pellente pellente eget. Lorem ipsum dolor slo onsec Vivamus....</p></article>
    <article class="feature"><div class="feature-head"><span class="feature-icon"><svg width="12" height="14"><rect x="1" y="1" width="10" height="12" fill="none" stroke="#fff"/></svg></span><h3 class="feature-title">Community Highlights</h3></div><p class="feature-text">Lorem ipsum dolor slo onsec tueraliquet Morbi nec In Curabitur lreaoreet nisl lorem in pellente pellente eget. Lorem ipsum dolor slo onsec Vivamus....</p></article>
  </div>
</section>
</body>
</html>
```